Medical Company in need of Modern business card design for new Wound Care clinic.

Modern business card design for our Woundcare company. Logo and description of services can be found on our website; https://www.tornvel-skinheal.com/

```html
<!DOCTYPE html>
<html lang="en">
<head>
<meta charset="utf-8">
<title>Tornvel Skinheal Business Card</title>
<link rel="stylesheet" href="https://fonts.googleapis.com/css2?family=Montserrat:wght@400;500;700&display=swap">
<style>
  :root {
    --backdrop: #383838;
    --card: #161616;
    --emboss: #0b0b0b;
    --gold: #d9a03c;
    --gold-light: #e9b85a;
    --ink: #f2f2f2;
  }
  * { box-sizing: border-box; margin: 0; padding: 0; }
  html, body {
    width: 1200px; height: 1200px; overflow: hidden;
    background: var(--backdrop);
    font-family: "Montserrat", sans-serif;
  }
  .stage {
    position: relative; width: 1200px; height: 1200px;
    display: flex; flex-direction: column; align-items: center; justify-content: center; gap: 70px;
  }
  .card {
    position: relative; width: 700px; height: 400px;
    background: var(--card);
    border-radius: 28px;
    border: 3px solid var(--gold);
    box-shadow: 0 18px 40px rgba(0,0,0,0.45);
    overflow: hidden;
  }
  .wordmark {
    display: flex; align-items: center; gap: 14px;
    font-weight: 500; letter-spacing: 0.32em; text-transform: uppercase;
  }
  .wordmark__mark { width: 16px; height: 16px; background: var(--gold); }
  .card--front .wordmark {
    position: absolute; top: 50%; left: 50%; transform: translate(-50%, -50%);
    font-size: 32px; color: var(--emboss);
  }
  .card--front .wordmark__mark { background: var(--emboss); width: 22px; height: 22px; }
  .card--back .wordmark {
    position: absolute; top: 70px; right: 60px;
    font-size: 22px; color: var(--ink);
  }
  .services { position: absolute; left: 54px; top: 168px; color: var(--ink); }
  .services__title { color: var(--gold); font-weight: 700; font-size: 24px; margin-bottom: 10px; }
  .services__list { list-style: none; font-size: 15px; line-height: 1.45; }
  .services__list li { position: relative; padding-left: 16px; }
  .services__list li::before {
    content: ""; position: absolute; left: 0; top: 9px;
    width: 6px; height: 6px; border-radius: 50%; background: var(--gold-light);
  }
  .contact { position: absolute; left: 410px; top: 168px; color: var(--ink); }
  .contact__name { color: var(--gold); font-weight: 700; font-size: 30px; line-height: 1.05; }
  .contact__role { font-size: 15px; margin-bottom: 22px; }
  .contact__row { display: flex; align-items: center; gap: 12px; font-size: 15px; margin-bottom: 8px; }
  .contact__row svg { width: 18px; height: 18px; flex: none; }
</style>
</head>
<body>
<main class="stage">
  <section class="card card--front">
    <div class="wordmark"><span class="wordmark__mark"></span>Tornvel Skinheal</div>
  </section>

  <section class="card card--back">
    <div class="wordmark"><span class="wordmark__mark"></span>Tornvel Skinheal</div>

    <div class="services">
      <h2 class="services__title">Our Services</h2>
      <ul class="services__list">
        <li>Hyperbaric Oxygen Therapy<br>(HBO): A Cornerstone of<br>Advanced Wound Care</li>
        <li>Debridement</li>
        <li>Advanced Wound Dressings</li>
        <li>Bio-engineered Skin Substitutes</li>
        <li>Compression Therapy and</li>
        <li>Edema Management</li>
      </ul>
    </div>

    <div class="contact">
      <h1 class="contact__name">Darren Holt</h1>
      <p class="contact__role">Managing Director</p>
      <p class="contact__row">
        <svg viewBox="0 0 24 24" aria-hidden="true"><path fill="var(--gold)" d="M6.6 10.8a15.1 15.1 0 0 0 6.6 6.6l2.2-2.2a1 1 0 0 1 1-.25 11.4 11.4 0 0 0 3.6.57 1 1 0 0 1 1 1V20a1 1 0 0 1-1 1A17 17 0 0 1 3 4a1 1 0 0 1 1-1h3.5a1 1 0 0 1 1 1c0 1.25.2 2.45.57 3.6a1 1 0 0 1-.25 1z"/></svg>
        555.014.2290
      </p>
      <p class="contact__row">
        <svg viewBox="0 0 24 24" aria-hidden="true"><path fill="var(--gold)" d="M3 5h18v14H3z"/><path fill="none" stroke="var(--card)" stroke-width="1.6" d="M3 5l9 7 9-7"/></svg>
        info@tornvel-skinheal.com
      </p>
      <p class="contact__row">
        <svg viewBox="0 0 24 24" aria-hidden="true"><circle cx="12" cy="12" r="9" fill="none" stroke="var(--gold)" stroke-width="2"/><path fill="none" stroke="var(--gold)" stroke-width="1.5" d="M3 12h18M12 3c3 3 3 15 0 18M12 3c-3 3-3 15 0 18"/></svg>
        www.tornvel-skinheal.com
      </p>
    </div>
  </section>
</main>
</body>
</html>
```